Book Cover Design - Uncovering Weight Loss Secrets

I need a book cover design for a book called 'Folding The Map'. It is a book that goes through all of the secrets to weight loss, without any crazy shakes or workouts or pills or potions. The book is really focused on helping people understand that Weight loss is simple and has more to do with our mindset as well as the food we were eating. It is about taking personal responsibility not looking for the next fancy revolutionary product that is going to help them magically melt the fat away. The book is pragmatic in nature and breaks down in simple terms how we can lose weight and keep it off for the rest of our lives. It shows the user that it is simple to lose weight, but it takes effort. They should stop looking for a quick fix when it comes to weight loss but instead eat healthy for the rest of their lives.
The book is intended to be hard-hitting no holds barred approach. The book has the same title as my business name. I will attach the current logo that we use in the business. This doesn't need to be on the front of the book maybe at the back down the bottom somewhere.
I am looking to have both an e-book cover and a standard printed book cover.
I don't have any colours in mind, my logo can be adapted to be different colours or just white.
The message that I am wanting people to feel when they see my book, is that all these Weightloss fads are a joke, that I know the secrets that will get them to their weight loss goal even if they fail at everything else before.
On the cover it should say the following.
FOLDING THE MAP
Uncovering the Weight Loss Secrets
The big companies have been trying to keep hidden for years!
COLIN MAYHEW
People who have failed many times trying to lose weight & need help
Weight Loss

```html
<!DOCTYPE html>
<html lang="en">
<head>
<meta charset="utf-8">
<title>Folding The Map – Weight Loss Secrets</title>
<link rel="stylesheet" href="https://fonts.googleapis.com/css2?family=Montserrat:wght@700;800&family=Roboto+Condensed:wght@700&family=Hind:wght@500&display=swap">
<style>
  :root {
    --page-bg: #e9e9e8;
    --cover-brown: #3d2818;
    --cover-brown-deep: #2a1b10;
    --title-yellow: #f7e51c;
    --subtitle-yellow: #f2e36a;
    --headline-white: #ffffff;
    --band-black: #0c0c0c;
    --photo-warm: #6b4a2e;
    --photo-green: #4d6a2c;
    --photo-table: #b98a5c;
  }
  * { margin: 0; padding: 0; box-sizing: border-box; }
  html, body {
    width: 1200px;
    height: 860px;
    overflow: hidden;
    background: var(--page-bg);
  }
  .stage {
    position: relative;
    width: 1200px;
    height: 860px;
  }
  .book-cover {
    position: absolute;
    left: 375px;
    top: 31px;
    width: 450px;
    height: 798px;
    background: var(--cover-brown);
    overflow: hidden;
    text-align: center;
  }
  .book-title {
    position: absolute;
    top: 50px;
    left: 0;
    width: 100%;
    font-family: "Roboto Condensed", "Arial Narrow", sans-serif;
    font-weight: 700;
    font-size: 50px;
    line-height: 1;
    color: var(--title-yellow);
    letter-spacing: 0.5px;
  }
  .headline {
    position: absolute;
    left: 0;
    width: 100%;
    font-family: "Montserrat", Arial, sans-serif;
    font-weight: 700;
    color: var(--headline-white);
    line-height: 1;
  }
  .headline--top {
    top: 118px;
    font-size: 45px;
    letter-spacing: -0.5px;
  }
  .headline--main {
    top: 172px;
    font-size: 66px;
    letter-spacing: 0;
  }
  .tagline {
    position: absolute;
    top: 268px;
    left: 0;
    width: 100%;
    font-family: "Hind", Arial, sans-serif;
    font-weight: 500;
    font-size: 22px;
    line-height: 32px;
    color: var(--subtitle-yellow);
  }
  .cover-photo {
    position: absolute;
    top: 410px;
    left: 0;
    width: 100%;
    height: 310px;
  }
  .author-band {
    position: absolute;
    left: 0;
    bottom: 0;
    width: 100%;
    height: 78px;
    background: var(--band-black);
    display: flex;
    align-items: center;
    justify-content: center;
  }
  .author-name {
    font-family: "Montserrat", Arial, sans-serif;
    font-weight: 700;
    font-size: 22px;
    color: var(--title-yellow);
    letter-spacing: 0.5px;
  }
</style>
</head>
<body>
  <main class="stage">
    <section class="book-cover">
      <h1 class="book-title">FOLDING THE MAP</h1>
      <p class="headline headline--top">WEIGHT LOSS</p>
      <p class="headline headline--main">SECRETS</p>
      <p class="tagline">For Losing All The Weight<br>You Want &amp; Keeping It Off Forever<br>No Matter What<br>You Have Tried in The Past</p>

      <svg class="cover-photo" viewBox="0 0 450 310" role="img" aria-label="Photo of a steaming bowl of fresh salad with a yellow measuring tape and a fork on a wooden table">
        <defs>
          <radialGradient id="bowl-glow" cx="0.45" cy="0.45" r="0.55">
            <stop offset="0" stop-color="var(--photo-green)"/>
            <stop offset="0.55" stop-color="var(--photo-warm)"/>
            <stop offset="1" stop-color="var(--cover-brown)"/>
          </radialGradient>
          <linearGradient id="table-tone" x1="0" y1="0" x2="0" y2="1">
            <stop offset="0" stop-color="var(--cover-brown)"/>
            <stop offset="0.7" stop-color="var(--photo-table)" stop-opacity="0.7"/>
            <stop offset="1" stop-color="var(--photo-table)"/>
          </linearGradient>
        </defs>
        <rect width="450" height="310" fill="url(#table-tone)"/>
        <rect width="450" height="310" fill="url(#bowl-glow)" opacity="0.85"/>
      </svg>

      <footer class="author-band">
        <span class="author-name">COLIN MAYHEW</span>
      </footer>
    </section>
  </main>
</body>
</html>
```